Lumo Vance IT company Soho london Stationary

We've just had a new logo designed on Gallow Pier and we now need some Stationary to go with it.
We're a small IT support firm supporting Design companies in Soho London. Most of our clients work on Vorls and a relatively creative so we want a relatively informal design on our stationary to reflect this.
We'd like to stick with the green in the logo but we're not adverse to adding another few colours to the palette.
Please see the attached file for our logo and not our website.

It Company

```html
<!DOCTYPE html>
<html lang="en">
<head>
<meta charset="utf-8">
<title>Lumo Vance — Business Card</title>
<link href="https://fonts.googleapis.com/css2?family=Open+Sans:wght@300;400;600;700&display=swap" rel="stylesheet">
<style>
  :root {
    --backdrop: #e6e2dc;
    --card-top: #22262c;
    --card-bottom: #0b0d10;
    --lime: #a8cf16;
    --lime-light: #bcdc2a;
    --lime-deep: #8fbf12;
    --white: #ffffff;
    --muted: #b9bec6;
    --frame: #3c4250;
  }
  * { margin: 0; padding: 0; box-sizing: border-box; }
  html, body {
    width: 900px; height: 1200px; overflow: hidden;
    background: var(--backdrop);
    font-family: "Open Sans", Arial, sans-serif;
  }
  .canvas { position: relative; width: 900px; height: 1200px; }

  .card {
    position: absolute; left: 72px; width: 756px; height: 420px;
    overflow: hidden;
    background: linear-gradient(160deg, var(--card-top) 0%, #15181d 50%, var(--card-bottom) 100%);
    box-shadow: 0 10px 24px rgba(0,0,0,0.35);
  }
  .card--front { top: 70px; }
  .card--back { top: 690px; }

  .wordmark {
    display: flex; align-items: center; gap: 14px;
    color: var(--lime); font-weight: 700; letter-spacing: -1px; white-space: nowrap;
  }
  .wordmark__dot { border-radius: 50%; background: var(--lime); flex: none; }

  .card--front .wordmark {
    position: absolute; left: 0; right: 0; top: 158px;
    justify-content: center; font-size: 78px; line-height: 1;
  }
  .card--front .wordmark__dot { width: 22px; height: 22px; }

  /* back */
  .panel-frame {
    position: absolute; left: 330px; top: 18px; width: 450px; height: 300px;
    border-left: 7px solid var(--frame); border-bottom: 7px solid var(--frame);
  }
  .card--back .wordmark {
    position: absolute; left: 358px; top: 58px; font-size: 60px; line-height: 1;
  }
  .card--back .wordmark__dot { width: 16px; height: 16px; }

  .company-phone {
    position: absolute; left: 352px; top: 160px;
    display: flex; align-items: center; gap: 6px;
    color: var(--white); font-weight: 700; font-size: 19px;
  }
  .company-address {
    position: absolute; left: 348px; top: 205px;
    color: var(--lime); font-size: 19px; letter-spacing: 0.3px;
  }
  .company-email {
    position: absolute; left: 348px; top: 248px;
    color: var(--white); font-size: 19px;
  }
  .company-web {
    position: absolute; left: 552px; top: 252px;
    color: var(--muted); font-size: 20px;
  }

  .person-name {
    position: absolute; left: 218px; top: 20px; width: 220px; height: 80px;
    transform-origin: 0 0; transform: translate(80px, 0) rotate(90deg);
    display: flex; flex-direction: column; justify-content: center;
    font-size: 24px; letter-spacing: 10px; line-height: 1.4; white-space: nowrap;
  }
  .person-name__first { color: var(--lime); font-weight: 700; }
  .person-name__last { color: var(--white); font-weight: 400; }

  .person-role {
    position: absolute; left: 66px; top: 198px;
    color: var(--lime); font-size: 21px;
  }
  .person-block {
    position: absolute; left: 38px; top: 232px; width: 168px; height: 200px;
    background: linear-gradient(160deg, var(--lime-light), var(--lime-deep));
  }
  .person-phone {
    position: absolute; left: 22px; top: 14px;
    color: var(--white); font-weight: 700; font-size: 18px;
  }
  .person-email {
    position: absolute; left: 10px; top: 160px;
    color: var(--white); font-size: 13px;
  }
</style>
</head>
<body>
<main class="canvas">

  <section class="card card--front" aria-label="Card front">
    <div class="wordmark"><span class="wordmark__dot"></span>Lumo Vance</div>
  </section>

  <section class="card card--back" aria-label="Card back">
    <div class="panel-frame"></div>

    <div class="wordmark"><span class="wordmark__dot"></span>Lumo Vance</div>

    <div class="company-phone">
      <svg width="20" height="22" viewBox="0 0 20 22" aria-hidden="true">
        <path d="M5 2 L8 2 L9 7 L6.5 8.5 C7.5 11.5 9 14 11.5 16 L14 14 L18 16.5 L17 20 C9 20 2.5 12 3 3 Z" fill="none" stroke="#ffffff" stroke-width="1.8" stroke-linejoin="round"/>
      </svg>
      0203 555 0142
    </div>
    <div class="company-address">22 Harrow Lane , London , W1X 9ZQ.</div>
    <div class="company-email">info@lumo-vance.it</div>
    <div class="company-web">www.lumo-vance.it</div>

    <div class="person-name">
      <span class="person-name__first">TOBIN</span>
      <span class="person-name__last">REYES</span>
    </div>

    <div class="person-role">web designer</div>
    <div class="person-block">
      <div class="person-phone">0204 555 0187</div>
      <div class="person-email">tobin@lumo-vance.it</div>
    </div>
  </section>

</main>
</body>
</html>
```